Website for Youth Orchestra to sell tickets and attract young musicians

We are looking for a new website design for a Youth Orchestra; one of the best classical youth orchestras in the county. This project is the design only. <br/><br/>The website serves two main purposes:<br/>• Selling tickets for concerts and performances of the orchestra<br/>• Recruiting young musicians to do audition for the orchestra<br/>
Updates

Target Market(s)

Classical music lovers with a special interest in young upcoming musicians.
Young talented musicians

Number of Pages Required

2 page

Colors
ec1f27

Requirements
Must have
• - A Picture on the front page that promotes the main upcomming event
• - Attention for recruiting new musicians
• - Pictures with young musicians (white back ground, see examples)
• - Responsive
• - Please use the logo attached
Should not have
• The brown colors of the current website (kvb-veldhorst.example)

```html
<!DOCTYPE html>
<html lang="nl">
<head>
<meta charset="utf-8">
<title>kvb-veldhorst – Nieuwjaarsconcert</title>
<link rel="stylesheet" href="https://fonts.googleapis.com/css2?family=Oswald:wght@400;500&family=Open+Sans:wght@400;700&display=swap">
<style>
  :root {
    --brand-red: #ec1f27;
    --rule-red: #e8636a;
    --ink: #1f1f1f;
    --text: #212121;
    --paper: #ffffff;
    --header-line: #e3e3e3;
    --poster-lilac: #e2d3e9;
    --poster-orange: #ef5a2a;
  }
  * { box-sizing: border-box; margin: 0; padding: 0; }
  html, body {
    width: 1200px; height: 680px; overflow: hidden;
    background: var(--paper);
    font-family: "Open Sans", Arial, sans-serif;
    color: var(--text);
  }
  .page { position: relative; width: 1200px; height: 680px; overflow: hidden; }

  .site-header {
    position: absolute; left: 0; top: 0; width: 1200px; height: 42px;
    border-bottom: 1px solid var(--header-line);
    display: flex; align-items: center;
  }
  .brand { display: flex; align-items: center; margin-left: 17px; }
  .brand-dot {
    width: 36px; height: 36px; border-radius: 50%;
    background: var(--brand-red); margin-right: 14px;
  }
  .brand-name {
    font-family: "Oswald", Arial, sans-serif; font-weight: 500;
    font-size: 16px; color: var(--ink);
  }
  .site-nav {
    position: absolute; right: 24px; top: 8px;
    display: flex; align-items: center; gap: 18px;
    font-size: 12px;
  }
  .nav-link { color: var(--ink); text-decoration: none; padding: 5px 8px; }
  .nav-link.is-active { background: var(--ink); color: var(--paper); }
  .search-icon { width: 16px; height: 16px; }

  .divider {
    position: absolute; left: 166px; width: 862px; height: 2px;
    background: var(--rule-red);
  }

  .feature { position: absolute; left: 166px; width: 862px; }
  .feature-media { position: absolute; left: 0; top: 0; width: 347px; }
  .feature-media.poster {
    height: 414px;
    background: linear-gradient(160deg, var(--poster-lilac) 0%, var(--poster-lilac) 40%, var(--poster-orange) 70%, var(--poster-lilac) 100%);
  }
  .feature-media.orchestra-mark { height: 200px; background: var(--brand-red); }

  .feature-body { position: absolute; left: 375px; top: 0; width: 487px; }
  .feature-title {
    font-family: "Oswald", Arial, sans-serif; font-weight: 400;
    font-size: 27.5px; line-height: 42px; color: var(--ink);
    text-transform: uppercase; letter-spacing: 0;
  }
  .feature-text p { font-size: 13.5px; line-height: 18px; margin-bottom: 14.6px; }
  .feature-text a { color: var(--ink); text-decoration: underline; }
  .feature-text strong { font-weight: 700; }
</style>
</head>
<body>
<div class="page">
  <header class="site-header">
    <div class="brand">
      <span class="brand-dot"></span>
      <span class="brand-name">kvb-veldhorst</span>
    </div>
    <nav class="site-nav">
      <a class="nav-link is-active" href="#">Home</a>
      <a class="nav-link" href="#">Events</a>
      <svg class="search-icon" viewBox="0 0 16 16" aria-label="Zoeken">
        <circle cx="6.5" cy="6.5" r="4.5" fill="none" stroke="#1f1f1f" stroke-width="1.8"/>
        <line x1="10" y1="10" x2="14.5" y2="14.5" stroke="#1f1f1f" stroke-width="2"/>
      </svg>
    </nav>
  </header>

  <div class="divider" style="top:50px"></div>

  <section class="feature" style="top:76px">
    <div class="feature-media poster" role="img" aria-label="Affiche van het nieuwjaarsconcert met een champagneglas en kleurige bubbels"></div>
    <div class="feature-body" style="top:14px">
      <h2 class="feature-title">Kaartverkoop KVB Nieuwjaarsconcert 12 januari 2020 gestart!</h2>
      <div class="feature-text" style="margin-top:24px">
        <p>Natuurlijk weer met de traditionele bubbels en bollen!</p>
        <p>Volwassenen € 17,00</p>
        <p>t/m 18 jr en JKP € 13,50</p>
        <p>t/m 14 jr € 0,00</p>
        <p>Voor verkoop aan de kassa geldt een toeslag van € 2,00</p>
        <p>Voor meer informatie en kaartverkoop klik <a href="#">hier</a>.</p>
        <p>Wees er snel bij, dit concert raakt altijd uitverkocht!</p>
        <p>Click here for details: <a href="#">Events</a></p>
      </div>
    </div>
  </section>

  <div class="divider" style="top:553px"></div>

  <section class="feature" style="top:580px">
    <div class="feature-media orchestra-mark" role="img" aria-label="Rood beeldvlak met de naam van het jeugdorkest"></div>
    <div class="feature-body" style="top:14px">
      <h2 class="feature-title">Kom bij ons</h2>
      <div class="feature-text" style="margin-top:14px">
        <p>Ben je van plan lid te worden van ons orkest? Kom dan langs! Op elke KVB-repetitie ben je <strong>van harte uitgenodigd</strong> om met eigen oren &amp; ogen te</p>
      </div>
    </div>
  </section>
</div>
</body>
</html>
```